Android Shop Depot Listing Screenshot Design

We would like to create new screenshots for our Android app in the Shop Depot to A/B test against the current version.

You can view our current Android Shop Depot listing here: https://shop.trelvani.com/store/apps/details?id=com.quorvix.android&hl=en

Attached I have added screenshots of the app that I would like to be included. Please edit the screenshots to generic text (e.g. John Smith, 123 Main St, etc.).

You can use the same text we have in the current ones. For text for the criminal screenshot please view our iOS Kiosk Hub listing: https://apps.mondrelo.com/us/app/quorvix-background-check/id918274650?mt=8

If you want to come up with new text please feel free to!

I also attached a few examples of other app screenshots that we like.

Android ShopDepot Listing Guidelines: https://help.trelvani.com/trelvanishop/android-developer/answer/5520931?hl=en

Industry/Entity Type

Store

Font styles to use
Sans Serif

Colors
f0f0f0

Requirements
Must have
• ~Generic names and data like "John Smith", "54 Main St. Springfield, NJ 09876"
• ~Screenshot for Person Search, Criminal Records, Phone Search, Email Search, and Property Search. In that order.
• ~Headlines either the ones used in our current screenshots (https://shop.trelvani.com/store/apps/details?id=com.quorvix.android&hl=en) or new ones you come up with.
• ~Must meet Android screenshot guidelines.
• ~Optimized for downloads.
• Must use following color palette:
• Dark purple #3B2469
• Light purple #7E6F9C
• Very dark gray #333333
• Dark gray #666666
• Gray #999999
• Blue gray #CFD9DE
• Green #5CB85C
• Navy #003577
• Yellow #F3B607
• Magenta #F0386B

```html
<!DOCTYPE html>
<html lang="en">
<head>
<meta charset="utf-8">
<title>Design 3 – Shop Depot listing screenshots</title>
<link href="https://fonts.googleapis.com/css2?family=Roboto:wght@400;500;700&display=swap" rel="stylesheet">
<style>
:root{
  --board:#e0e7ea;
  --card:#ffffff;
  --dark-purple:#3B2469;
  --light-purple:#7E6F9C;
  --ink:#333333;
  --ink-mid:#666666;
  --ink-soft:#999999;
  --blue-gray:#CFD9DE;
  --green:#5CB85C;
  --navy:#003577;
  --yellow:#F3B607;
  --magenta:#F0386B;
  --panel-top:#3a2580;
  --panel-bottom:#2d5db6;
}
*{box-sizing:border-box;margin:0;padding:0}
html,body{width:1200px;height:1200px;overflow:hidden}
body{background:var(--board);font-family:"Roboto",sans-serif;color:var(--ink);position:relative}
.board-title{position:absolute;left:94px;top:384px;font-size:25px;font-weight:400;color:#1b1b1b}
.board-card{position:absolute;left:95px;top:425px;width:1012px;height:384px;background:var(--card);box-shadow:0 1px 3px rgba(0,0,0,.12)}
.panel{position:absolute;top:24px;width:190px;height:336px;overflow:hidden;
  background:linear-gradient(180deg,var(--panel-top) 0%,#33399a 55%,var(--panel-bottom) 100%)}
.panel-headline{position:absolute;top:22px;left:0;width:100%;text-align:center;color:#fff;font-size:12.4px;font-weight:500;line-height:15.5px}
.prop{position:absolute;background:linear-gradient(160deg,#4d5570,#2a3048);opacity:.85}
.phone{position:absolute;left:23px;top:68px;width:143px;height:300px;background:#f5f5f7;border-radius:16px;border:1px solid #d9dbe0}
.phone-cam{position:absolute;left:23px;top:10px;width:5px;height:5px;border-radius:50%;background:#222}
.phone-speaker{position:absolute;left:64px;top:11px;width:16px;height:3px;border-radius:2px;background:#222}
.screen{position:absolute;left:7px;top:28px;width:128px;height:272px;background:#fff;overflow:hidden;font-size:5px}
.status{height:8px;background:#2c1a52;color:#cfc6e6;font-size:4.6px;text-align:right;padding-right:3px;line-height:8px}
.appbar{height:20px;background:var(--dark-purple);color:#fff;font-size:6.6px;font-weight:500;display:flex;align-items:center;padding:0 4px;gap:8px}
.appbar .icons{margin-left:auto;display:flex;gap:6px;font-size:6px}
.hero{background:var(--light-purple);color:#fff;text-align:center;position:relative;padding-top:6px}
.hero-cut{position:absolute;left:0;bottom:0;width:128px;height:14px}
.hero .name{font-size:8px;font-weight:500}
.hero .sub{font-size:5.4px;color:#e6e1f0;line-height:8px}
.avatar{width:42px;height:42px;border-radius:50%;margin:4px auto 0;position:relative;z-index:2;border:2px solid #fff;background:linear-gradient(160deg,#8a8f99,#4a4f58)}
.tap{text-align:center;font-size:5px;color:var(--dark-purple);font-weight:500;margin:6px 0 4px}
.row{display:flex;align-items:center;height:23px;border-top:1px solid #eee;padding:0 5px;gap:7px;font-size:5px;color:var(--dark-purple)}
.row .ic{width:14px;height:14px;border-radius:50%;background:var(--dark-purple)}
.row .badge{margin-left:auto;width:10px;height:10px;border-radius:50%;background:var(--magenta);color:#fff;font-size:4.4px;text-align:center;line-height:10px}
.row .chev{width:9px;text-align:right;font-size:9px;color:var(--dark-purple)}
.row .chev.solo{margin-left:auto}
.sec-title{font-size:8.4px;color:var(--dark-purple);padding:0 2px;margin-top:4px}
.lbl{font-size:4.6px;color:var(--ink-soft);text-transform:uppercase;padding:0 2px;margin-top:7px}
.val{font-size:5px;color:var(--ink);padding:0 2px;margin-top:2px}
.fab{position:absolute;width:19px;height:19px;border-radius:50%;background:var(--green);box-shadow:0 1px 3px rgba(0,0,0,.3)}
.fab::after{content:"";position:absolute;left:6px;top:7px;width:7px;height:5px;border-top:1px solid #fff;border-bottom:1px solid #fff}
.map{background:linear-gradient(135deg,#e4e6dc,#d6dcd0)}
.tabs{height:12px;background:#6a5c92;display:flex;align-items:center;justify-content:center;font-size:4px;color:#fff;font-weight:700;gap:8px}
.tabs span{opacity:.5;font-weight:400}
.gray-bar{background:#eceef0;text-align:center;font-size:4.8px;color:var(--ink-mid);height:10px;line-height:10px;margin-top:6px}
</style>
</head>
<body>
<h1 class="board-title">Design 3</h1>
<section class="board-card">

  <!-- Person search -->
  <article class="panel" style="left:24px">
    <h2 class="panel-headline">Run background checks<br>from anywhere</h2>
    <div class="prop" role="img" aria-label="Coffee mug on desk" style="left:170px;top:180px;width:30px;height:110px;border-radius:4px"></div>
    <div class="phone">
      <div class="phone-cam"></div><div class="phone-speaker"></div>
      <div class="screen">
        <div class="status">5:03 PM</div>
        <div class="appbar"><span>←</span><span>Person Report</span><span class="icons"><span>🔔</span><span>?</span><span>⋮</span></span></div>
        <div class="hero" style="height:98px">
          <div class="name">John Smith</div>
          <div class="sub">54 Main St, FL 2, Springfield<br>NJ 09876</div>
          <div class="sub" style="font-size:6px">Age 45</div>
          <div class="avatar" role="img" aria-label="Profile photo"></div>
          <svg class="hero-cut" viewBox="0 0 128 14" preserveAspectRatio="none"><polygon points="0,14 128,0 128,14" fill="#fff"/></svg>
        </div>
        <div class="tap">Tap a section below to explore</div>
        <div class="row"><span class="ic"></span>Personal Overview<span class="chev solo">›</span></div>
        <div class="row"><span class="ic"></span>Contact Information<span class="badge">6</span><span class="chev">›</span></div>
        <div class="row"><span class="ic"></span>Address History<span class="badge">18</span><span class="chev">›</span></div>
        <div class="row"><span class="ic"></span>Relatives<span class="badge">7</span><span class="chev">›</span></div>
      </div>
    </div>
  </article>

  <!-- Phone search -->
  <article class="panel" style="left:218px">
    <h2 class="panel-headline">Find out who an unknown<br>caller is in seconds</h2>
    <div class="prop" role="img" aria-label="Papers and desk objects" style="left:160px;top:40px;width:40px;height:260px;background:linear-gradient(170deg,#e9eaf0,#5a6075)"></div>
    <div class="phone">
      <div class="phone-cam"></div><div class="phone-speaker"></div>
      <div class="screen">
        <div class="status">5:10 PM</div>
        <div class="appbar"><span>←</span><span>Phone Report</span><span class="icons"><span>▤</span><span>?</span></span></div>
        <div class="hero" style="height:84px">
          <div class="sub" style="text-decoration:underline;font-size:5.6px">(555)-010-0199</div>
          <div class="name" style="font-size:7.6px">Dorian Pellham</div>
          <div style="width:40px;height:40px;border-radius:50%;background:#fff;margin:4px auto 0;position:relative;z-index:2;display:flex;align-items:center;justify-content:center">
            <svg width="22" height="22" viewBox="0 0 24 24"><path fill="#3B2469" d="M6.6 10.8c1.4 2.8 3.8 5.1 6.6 6.6l2.2-2.2c.3-.3.7-.4 1-.2 1.1.4 2.3.6 3.6.6.6 0 1 .4 1 1V20c0 .6-.4 1-1 1C10.6 21 3 13.4 3 4c0-.6.4-1 1-1h3.5c.6 0 1 .4 1 1 0 1.3.2 2.5.6 3.6.1.3 0 .7-.2 1z"/></svg>
          </div>
          <svg class="hero-cut" viewBox="0 0 128 14" preserveAspectRatio="none"><polygon points="0,14 128,0 128,14" fill="#fff"/></svg>
        </div>
        <div class="sec-title">Phone Overview</div>
        <div class="lbl">Spam score</div>
        <div style="margin:6px 3px 0;border:1px solid var(--yellow);height:41px;text-align:center;color:var(--yellow)">
          <div style="font-size:12px;margin-top:8px">10%</div>
          <div style="font-size:5.6px">Questionable Caller</div>
        </div>
        <div class="lbl" style="margin-top:10px">Location of area code</div>
        <div class="map" role="img" aria-label="Map of area code location" style="height:26px;margin-top:4px"></div>
        <div class="fab" style="left:104px;top:206px"></div>
      </div>
    </div>
  </article>

  <!-- Criminal records -->
  <article class="panel" style="left:411px">
    <h2 class="panel-headline">Find shocking information like<br>Criminal &amp; Traffic Records</h2>
    <div class="prop" role="img" aria-label="Typewriter on desk" style="left:0;top:150px;width:40px;height:190px"></div>
    <div class="prop" role="img" aria-label="Typewriter on desk" style="left:168px;top:140px;width:22px;height:190px"></div>
    <div class="phone">
      <div class="phone-cam"></div><div class="phone-speaker"></div>
      <div class="screen">
        <div class="status">5:08 PM</div>
        <div class="appbar"><span>←</span><span>ROWAN KETTERING</span><span class="icons"><span>🔔</span><span>?</span><span>⋮</span></span></div>
        <div class="tabs"><span>OWNERS</span>CRIMINAL &amp; TRAFFIC RECORDS<span>BANKR</span></div>
        <div class="lbl" style="margin-top:3px">Offense date</div><div class="val">Feb 24, 2009</div>
        <div class="lbl">Description of offense</div><div class="val">AGGRAVATED ASSAULT, ATTEMPT TO COMMIT</div>
        <div class="lbl">Offense type</div><div class="val">Department Of Correction</div>
        <div class="lbl">Case number</div><div class="val">N/A</div>
        <div class="lbl">Agency</div><div class="val">N/A</div>
        <div class="lbl">Date</div><div class="val">N/A</div>
        <div class="lbl">Offense details</div><div class="val">AGGRAVATED ASSAULT, ATTEMPT TO COMMIT</div>
        <div class="lbl">Disposition</div><div class="val">N/A</div>
        <div class="lbl">Level</div><div class="val">F</div>
      </div>
    </div>
  </article>

  <!-- Email search -->
  <article class="panel" style="left:605px">
    <h2 class="panel-headline">Check out hidden social<br>media profiles</h2>
    <div class="prop" role="img" aria-label="Record player on desk" style="left:0;top:120px;width:30px;height:210px"></div>
    <div class="prop" role="img" aria-label="Desk gears" style="left:170px;top:250px;width:20px;height:70px;border-radius:50%"></div>
    <div class="phone">
      <div class="phone-cam"></div><div class="phone-speaker"></div>
      <div class="screen">
        <div class="status">5:11 PM</div>
        <div class="appbar"><span>←</span><span>Email Report</span><span class="icons"><span>🔔</span><span>?</span></span></div>
        <div class="hero" style="height:74px">
          <div class="sub" style="text-decoration:underline;font-size:5.4px;color:#d8d2ea">marlo.vance@mailbox.test</div>
          <div class="avatar" role="img" aria-label="Profile photo" style="margin-top:3px"></div>
          <svg class="hero-cut" viewBox="0 0 128 14" preserveAspectRatio="none"><polygon points="0,14 128,0 128,14" fill="#fff"/></svg>
        </div>
        <div class="sec-title">Email Overview</div>
        <div class="lbl" style="margin-top:4px">Owner</div><div class="val">Marlo Vance</div>
        <div class="gray-bar">ALIASES</div>
        <div style="margin:6px 3px 0;border:1px solid #e2e2e2;height:46px;text-align:center">
          <div style="width:12px;height:10px;background:#ccc;margin:8px auto 5px;border-radius:1px"></div>
          <div style="font-size:4.4px;font-weight:700">No Aliases Were Found</div>
          <div style="font-size:4px;color:var(--ink-mid)">We searched for aliases, but there was no data.</div>
        </div>
        <div class="sec-title" style="margin-top:14px">Social Media &amp; Websites</div>
        <div class="fab" style="left:101px;top:188px"></div>
      </div>
    </div>
  </article>

  <!-- Property search -->
  <article class="panel" style="left:798px">
    <h2 class="panel-headline">Know more about a property<br>you plan to buy or rent</h2>
    <div class="prop" role="img" aria-label="Desk objects" style="left:0;top:110px;width:26px;height:90px;border-radius:50%"></div>
    <div class="phone">
      <div class="phone-cam"></div><div class="phone-speaker"></div>
      <div class="screen">
        <div class="status">5:13 PM</div>
        <div class="appbar"><span>←</span><span>48 Larkfield DR B…</span><span class="icons"><span>🔔</span><span>?</span></span></div>
        <div class="map" role="img" aria-label="Map of property location" style="height:46px"></div>
        <div class="lbl" style="margin-top:8px">Sales price</div><div class="val">$350,000</div>
        <div class="lbl">Bedrooms</div><div class="val">N/A</div>
        <div class="lbl">Bathrooms</div><div class="val">N/A</div>
        <div class="lbl">Building area</div><div class="val">1,248 Sq. Ft.</div>
        <div class="lbl">Property description</div>
        <div class="val" style="font-size:4.6px;line-height:5.6px"><b>48 Larkfield DR</b> is a property located in <b>Brenton, NJ</b>. It is owned by HALVERS, PETER J &amp; ANNA M. It has approximately <b>1,248 Sq. Ft.</b> It was last recorded in <b>2016</b>, where the sales price was <b>$350,000</b>.</div>
        <div class="sec-title" style="margin-top:6px">County Assessor Records</div>
        <div class="fab" style="left:104px;top:222px"></div>
      </div>
    </div>
  </article>

</section>
</body>
</html>
```